FR banner

we need a banner design (36"x120" horizontal) that will be displayed on a local high school baseball field. My company ( Crestwell Prints Co) has been producing signage for the Fernmoor Ridge community since 2009. We would like to communicate that we do more than banners. The final design should include the slogan "Signs Shirts Swag" and our Logo.

Target Market(s)

companies, teams, events, shirt and other marketing items.

Industry/Entity Type

Sign, Print,

Font styles to use
Sans Serif

Requirements
Should not have
• no baseball content.

```html
<!DOCTYPE html>
<html lang="en">
<head>
<meta charset="utf-8">
<title>Crestwell Prints Co — Field Banner</title>
<link rel="stylesheet" href="https://fonts.googleapis.com/css2?family=Archivo:wdth,wght@62..125,100..900&display=swap">
<style>
  :root {
    --ink: #000000;
    --paper: #ffffff;
    --signal-red: #ef2641;
  }
  html, body {
    margin: 0;
    padding: 0;
    width: 1200px;
    height: 360px;
    overflow: hidden;
    background: var(--paper);
  }
  .banner {
    position: relative;
    width: 1200px;
    height: 360px;
    overflow: hidden;
    background: var(--paper);
  }
  .banner-art {
    position: absolute;
    inset: 0;
    width: 1200px;
    height: 360px;
  }
  .shape-ink { fill: var(--ink); }
  .shape-red { fill: var(--signal-red); }
  .accent-stripe {
    stroke: var(--ink);
    stroke-width: 4;
    stroke-linecap: square;
  }
  .slogan-bar { fill: var(--ink); }
  .slogan-word {
    fill: var(--paper);
    font-family: "Archivo", sans-serif;
    font-weight: 900;
    font-stretch: 125%;
    font-size: 76px;
  }
  .brand-name {
    fill: var(--ink);
    font-family: "Archivo", sans-serif;
    font-weight: 900;
    font-stretch: 125%;
    font-size: 54px;
  }
  .brand-since {
    fill: var(--ink);
    font-family: "Archivo", sans-serif;
    font-weight: 700;
    font-size: 17px;
  }
</style>
</head>
<body>
<main class="banner">
  <svg class="banner-art" viewBox="0 0 1200 360" xmlns="http://www.w3.org/2000/svg" aria-labelledby="banner-title">
    <title id="banner-title">Crestwell Prints Co — Signs, Shirts, Swag — since 2009</title>

    <g class="corner-left">
      <polygon class="shape-ink" points="0,0 144,0 65,156 0,221"/>
      <polygon class="shape-red" points="144,0 233,0 112,113 65,156"/>
      <polygon class="shape-red" points="0,221 112,113 0,354"/>
    </g>

    <g class="corner-right">
      <polygon class="shape-ink" points="929,0 1200,0 1200,203 1078,113"/>
      <polygon class="shape-red" points="1078,113 1200,203 1200,360 1190,360"/>
      <polygon class="shape-ink" points="985,360 1144,247 1190,360"/>
    </g>

    <g class="accent-stripes">
      <line class="accent-stripe" x1="915" y1="7" x2="1041" y2="108"/>
      <line class="accent-stripe" x1="915" y1="30" x2="1015" y2="111"/>
      <line class="accent-stripe" x1="918" y1="57" x2="985" y2="112"/>
      <line class="accent-stripe" x1="920" y1="83" x2="960" y2="115"/>
      <line class="accent-stripe" x1="924" y1="105" x2="936" y2="116"/>
    </g>

    <g class="slogan">
      <path class="slogan-bar" d="M205,41 H585 A62,62 0 0 1 647,103 V121 H205 Z"/>
      <text class="slogan-word" x="224" y="108" textLength="337" lengthAdjust="spacingAndGlyphs">SIGNS</text>

      <path class="slogan-bar" d="M145,140 H525 A62,62 0 0 1 587,202 V219 H145 Z"/>
      <text class="slogan-word" x="163" y="207" textLength="377" lengthAdjust="spacingAndGlyphs">SHIRTS</text>

      <path class="slogan-bar" d="M92,238 H472 A62,62 0 0 1 534,300 V317 H92 Z"/>
      <text class="slogan-word" x="112" y="305" textLength="341" lengthAdjust="spacing">SWAG</text>
    </g>

    <g class="brand">
      <text class="brand-name" x="792" y="190" text-anchor="middle" textLength="296" lengthAdjust="spacingAndGlyphs">CRESTWELL</text>
      <text class="brand-name" x="792" y="252" text-anchor="middle" textLength="296" lengthAdjust="spacingAndGlyphs">PRINTS CO</text>
      <text class="brand-since" x="782" y="323" text-anchor="middle">since 2009</text>
    </g>
  </svg>
</main>
</body>
</html>
```